Need Poster Design for Indie Family Film

We need a poster for a indie family film and would like to see designs that should be elegant, bold and playful.

Willowmere follows the parallel stories of three Singaporeans dealing with familial love and loss: a young girl copes with her mother’s death by living in an imaginary world, a father struggles to reconcile with his estranged daughter before her wedding and a woman fails to convince her family of her desire to become a singer. Staring Marisol Teng, Delia Rahn with veterans Noriza Latef, Rashid Tembo and Gavin Lu and Trevor Pak

Target Market(s)

7-14 and Parents

Number of Pages Required

3 page

Font styles to use
Serif

Requirements
Must have
• Film Title: Willowmere
Nice to have
• The poster doesn't have to incorporate the photos and can use other design elements like illustrations.
Should not have
• Anything offensive and disturbing.

```html
<!DOCTYPE html>
<html lang="en">
<head>
<meta charset="utf-8">
<title>Willowmere – Film Poster</title>
<link rel="stylesheet" href="https://fonts.googleapis.com/css2?family=Roboto+Slab:wght@700;800&family=Source+Serif+4:wght@400&display=swap">
<style>
  :root {
    --leaf-dark: #1c0e06;
    --leaf-mid: #5a3114;
    --leaf-warm: #8a5222;
    --label-orange: #f4a21d;
    --ink-white: #ffffff;
    --band-black: #000000;
    --rule: rgba(255,255,255,0.22);
    --scene-light: #d9cfc4;
    --scene-orange: #f2a02c;
  }
  html, body {
    margin: 0;
    padding: 0;
    width: 849px;
    height: 1200px;
    overflow: hidden;
    background: var(--band-black);
  }
  .poster {
    position: relative;
    width: 849px;
    height: 1200px;
    overflow: hidden;
    font-family: "Roboto Slab", Georgia, serif;
    color: var(--ink-white);
  }
  .backdrop {
    position: absolute;
    inset: 0 0 165px 0;
    background:
      radial-gradient(ellipse at 55% 35%, var(--leaf-warm) 0%, var(--leaf-mid) 35%, transparent 75%),
      radial-gradient(ellipse at 20% 80%, #6b3a17 0%, transparent 55%),
      linear-gradient(180deg, #2a1509 0%, var(--leaf-mid) 45%, #3a1d0b 75%, var(--leaf-dark) 100%);
  }
  .directors {
    position: absolute;
    top: 0;
    left: 0;
    width: 100%;
    margin: 0;
    padding-top: 31px;
    text-align: center;
    font-weight: 700;
    font-size: 13px;
    line-height: 16px;
    letter-spacing: 0.3px;
    transform: translateY(-8px);
  }
  .feature-photo {
    position: absolute;
    left: 150px;
    top: 178px;
    width: 490px;
    height: 492px;
    border-radius: 4px;
    background: linear-gradient(90deg, rgba(217,207,196,0.55) 0%, rgba(217,207,196,0.35) 38%, rgba(242,160,44,0.75) 55%, rgba(242,160,44,0.8) 100%);
  }
  .title {
    position: absolute;
    top: 668px;
    left: 0;
    width: 100%;
    margin: 0;
    text-align: center;
    font-weight: 800;
    font-size: 92px;
    line-height: 1;
    letter-spacing: 1px;
    text-transform: uppercase;
  }
  .credits {
    position: absolute;
    top: 822px;
    left: 24px;
    width: 801px;
    height: 166px;
    box-sizing: border-box;
    padding-top: 18px;
    text-align: center;
    font-weight: 700;
    font-size: 12.4px;
    line-height: 21px;
    text-transform: uppercase;
    white-space: nowrap;
  }
  .credits::before,
  .credits::after {
    content: "";
    position: absolute;
    left: 88px;
    width: 700px;
    height: 1px;
    background: var(--rule);
  }
  .credits::before { top: 0; }
  .credits::after { bottom: 0; }
  .credits p { margin: 0; }
  .credits .gap { display: inline-block; width: 22px; }
  .credit-label { color: var(--label-orange); }
  .synopsis-band {
    position: absolute;
    left: 0;
    bottom: 0;
    width: 100%;
    height: 165px;
    background: var(--band-black);
  }
  .synopsis {
    margin: 30px auto 0;
    width: 640px;
    text-align: center;
    font-family: "Source Serif 4", Georgia, serif;
    font-size: 13px;
    line-height: 16.5px;
  }
</style>
</head>
<body>
<main class="poster">
  <div class="backdrop" role="img" aria-label="Close-up photograph of a dry brown leaf with glowing golden veins"></div>

  <p class="directors">DIR. CORINNE VALE, HAFIZ MORROW AND DARREN QUILL</p>

  <div class="feature-photo" role="img" aria-label="Photo of a waving schoolgirl standing beside a large orange mascot costume"></div>

  <h1 class="title">Willowmere</h1>

  <section class="credits">
    <p><span class="credit-label">Cast:</span> Noriza Latef, Rashid Tembo Gavin Lu, Delia Rahn, Marisol Teng</p>
    <p><span class="credit-label">Producer:</span> Darren Quill<span class="gap"></span><span class="credit-label">Co Directors:</span> Hafiz Morrow and Corinne Vale, Darren Quill</p>
    <p><span class="credit-label">Director of Photography:</span> Elton Marsh<span class="gap"></span><span class="credit-label">Camera Assistant:</span> Arif Sentosa</p>
    <p><span class="credit-label">Sound:</span> Safira Lind<span class="gap"></span><span class="credit-label">Editor:</span> Peter Alan Corwell</p>
    <p><span class="credit-label">Production Designer:</span> Jodie Fenn<span class="gap"></span><span class="credit-label">Production Art Assistant:</span> Amir Solano &amp; Julian Reyes</p>
    <p><span class="credit-label">Music Composer:</span> Wen Hollis and Tan Wei Ler<span class="gap"></span><span class="credit-label">Production Assistant:</span> Nadira Oakes</p>
    <p><span class="credit-label">Assistant Producer:</span> Carmen Yue<span class="gap"></span><span class="credit-label">Production Company:</span> Lanternfield Pictures</p>
  </section>

  <footer class="synopsis-band">
    <p class="synopsis">Willowmere follows the parallel stories of three Singaporeans dealing with familial love and loss: a young girl copes with her mother’s death by living in an imaginary world, a father struggles to reconcile with his estranged daughter before her wedding and a woman fails to convince her family of her desire to become a Getai singer. Staring Marisol Teng, Delia Rahn with veterans Noriza Latef, Rashid Tembo and Gavin Lu and Trevor Pak.</p>
  </footer>
</main>
</body>
</html>
```